Velmoxa AdAgency Presentation

We need ppt design for an ad agency re-branding, agency is based in Moscow, Russia. Our specifics is brand audit, consulting and strategy in web and offline.
We decided to do re-branding because our current agency does not answer the purpose and we need a kind of "second breath".
The idea of re-branding appeared because of many changes that happened in company: new clients, new projects level, new team.
So we'd like to promote company of changes and design should show this spirit as possible.
You may use info in attached pdf file (sorry for Russian language). Info is not so necessary, it will be replaced later.

Please use more colors than digital blue and grey!

Industry/Entity Type

Ad Agency

Requirements
Must have
• Logo is attached. Please choose one.

Ppt project should include:
- Front and last page design
- Heading and list design
- Page-separator design
- Diagram design
- Pics appearance

```html
<!DOCTYPE html>
<html lang="en">
<head>
<meta charset="utf-8">
<title>Velmoxa — Project Slide</title>
<link rel="stylesheet" href="https://fonts.googleapis.com/css2?family=Montserrat:wght@600&family=Questrial&display=swap">
<style>
  :root {
    --brand-blue: #29a9e0;
    --header-shape: #4db8e6;
    --rule-grey: #d3d5d7;
    --text-dark: #333333;
    --white: #ffffff;
    --frame-grey: #b9bdc1;
    --pattern-grey: #f1f2f3;
    --accent-orange: #f39200;
    --accent-green: #8cc63f;
    --accent-magenta: #e5007e;
    --accent-yellow: #ffd200;
  }
  * { margin: 0; padding: 0; box-sizing: border-box; }
  html, body { width: 1200px; height: 900px; overflow: hidden; background: var(--white); }
  .slide { position: relative; width: 1200px; height: 900px; overflow: hidden; background: var(--white); font-family: "Questrial", sans-serif; color: var(--text-dark); }

  .background-pattern { position: absolute; left: 900px; top: 200px; width: 300px; height: 600px; }

  .slide-header { position: absolute; left: 0; top: 0; width: 1200px; height: 86px; background: var(--brand-blue); overflow: hidden; }
  .slide-header__shape { position: absolute; left: 1092px; top: -6px; width: 96px; height: 84px; }
  .slide-header__rule { position: absolute; left: 0; top: 86px; width: 1200px; height: 7px; background: var(--rule-grey); display: flex; justify-content: flex-end; }
  .slide-header__accent { width: 60px; height: 7px; }
  .slide-header__accent--orange { background: var(--accent-orange); }
  .slide-header__accent--green { background: var(--accent-green); }
  .slide-header__accent--magenta { background: var(--accent-magenta); }
  .slide-header__accent--yellow { background: var(--accent-yellow); }
  .slide-title { position: absolute; left: 22px; top: 22px; font-family: "Montserrat", sans-serif; font-weight: 600; font-size: 35px; letter-spacing: 0.5px; color: var(--white); line-height: 1.2; }

  .content-block { position: absolute; left: 48px; width: 640px; }
  .content-block--first { top: 155px; }
  .content-block--second { top: 497px; }
  .content-block__heading { font-size: 23px; color: var(--brand-blue); line-height: 32px; -webkit-text-stroke: 0.5px var(--brand-blue); }
  .bullet-list { list-style: none; margin-top: 13px; }
  .bullet-list__item { position: relative; height: 48px; line-height: 32px; padding-left: 38px; font-size: 21px; color: var(--text-dark); }
  .bullet-list__arrow { position: absolute; left: 5px; top: 8px; width: 22px; height: 16px; }

  .screen-visual { position: absolute; left: 740px; width: 442px; height: 256px; border-radius: 10px 10px 4px 4px; background: linear-gradient(180deg, #e6e8ea 0%, #f2f2f2 45%, #f7f3df 70%, #b4b8bd 100%); box-shadow: inset 0 0 0 10px #2b2d30; }
  .screen-visual--first { top: 172px; }
  .screen-visual--second { top: 522px; }

  .copyright { position: absolute; left: 32px; top: 857px; font-size: 18px; color: var(--brand-blue); }

  .page-number { position: absolute; left: 1106px; top: 840px; width: 72px; height: 72px; border: 4px solid var(--frame-grey); border-radius: 10px; padding: 5px; background: var(--white); }
  .page-number__box { width: 100%; height: 100%; background: var(--brand-blue); border-radius: 4px; color: var(--white); font-family: "Montserrat", sans-serif; font-weight: 600; font-size: 25px; text-align: center; padding-top: 9px; }
</style>
</head>
<body>
<main class="slide">
  <svg class="background-pattern" viewBox="0 0 300 600" aria-hidden="true">
    <g fill="none" stroke="#f1f2f3" stroke-width="14">
      <rect x="30" y="20" width="250" height="250"/>
      <path d="M30 320H280M30 370H280M30 420H280M30 470H230M30 520H280"/>
      <path d="M70 80H240M70 130H240M70 180H200"/>
    </g>
  </svg>

  <header>
    <div class="slide-header">
      <svg class="slide-header__shape" viewBox="0 0 96 84" aria-hidden="true">
        <g fill="none" stroke="#4db8e6" stroke-width="5">
          <path d="M8 10H70L88 28V80H8Z"/>
          <path d="M20 36H76M20 50H76M20 64H60"/>
        </g>
      </svg>
    </div>
    <div class="slide-header__rule">
      <span class="slide-header__accent slide-header__accent--orange"></span>
      <span class="slide-header__accent slide-header__accent--green"></span>
      <span class="slide-header__accent slide-header__accent--magenta"></span>
      <span class="slide-header__accent slide-header__accent--yellow"></span>
    </div>
    <h1 class="slide-title">PROJECT TITLE HERE</h1>
  </header>

  <section class="content-block content-block--first">
    <h2 class="content-block__heading">Lorem ispum lorem ipsum dolor sit ispum lorem ipsum</h2>
    <ul class="bullet-list">
      <li class="bullet-list__item"><svg class="bullet-list__arrow" viewBox="0 0 22 16"><path d="M1 8H19M12 1L19 8L12 15" fill="none" stroke="#29a9e0" stroke-width="2.6"/></svg>Lorem ipsum dolor sit ispum Lorem ipsum dolor sit</li>
      <li class="bullet-list__item"><svg class="bullet-list__arrow" viewBox="0 0 22 16"><path d="M1 8H19M12 1L19 8L12 15" fill="none" stroke="#29a9e0" stroke-width="2.6"/></svg>Lorem ipsum lorem ipsum dolor sit ispum lorem ipsum</li>
      <li class="bullet-list__item"><svg class="bullet-list__arrow" viewBox="0 0 22 16"><path d="M1 8H19M12 1L19 8L12 15" fill="none" stroke="#29a9e0" stroke-width="2.6"/></svg>Lorem ipsum dolor sit ispum Lorem ipsum dolor sit</li>
      <li class="bullet-list__item"><svg class="bullet-list__arrow" viewBox="0 0 22 16"><path d="M1 8H19M12 1L19 8L12 15" fill="none" stroke="#29a9e0" stroke-width="2.6"/></svg>Lorem ipsum lorem ipsum dolor sit ispum lorem ipsum</li>
      <li class="bullet-list__item"><svg class="bullet-list__arrow" viewBox="0 0 22 16"><path d="M1 8H19M12 1L19 8L12 15" fill="none" stroke="#29a9e0" stroke-width="2.6"/></svg>Lorem ipsum dolor sit ispum Lorem ipsum dolor sit</li>
    </ul>
  </section>

  <div class="screen-visual screen-visual--first" role="img" aria-label="Laptop displaying a website project screenshot"></div>

  <section class="content-block content-block--second">
    <h2 class="content-block__heading">Lorem ispum lorem ipsum dolor sit ispum lorem ipsum</h2>
    <ul class="bullet-list">
      <li class="bullet-list__item"><svg class="bullet-list__arrow" viewBox="0 0 22 16"><path d="M1 8H19M12 1L19 8L12 15" fill="none" stroke="#29a9e0" stroke-width="2.6"/></svg>Lorem ipsum dolor sit ispum Lorem ipsum dolor sit</li>
      <li class="bullet-list__item"><svg class="bullet-list__arrow" viewBox="0 0 22 16"><path d="M1 8H19M12 1L19 8L12 15" fill="none" stroke="#29a9e0" stroke-width="2.6"/></svg>Lorem ipsum lorem ipsum dolor sit ispum lorem ipsum</li>
      <li class="bullet-list__item"><svg class="bullet-list__arrow" viewBox="0 0 22 16"><path d="M1 8H19M12 1L19 8L12 15" fill="none" stroke="#29a9e0" stroke-width="2.6"/></svg>Lorem ipsum dolor sit ispum Lorem ipsum dolor sit</li>
      <li class="bullet-list__item"><svg class="bullet-list__arrow" viewBox="0 0 22 16"><path d="M1 8H19M12 1L19 8L12 15" fill="none" stroke="#29a9e0" stroke-width="2.6"/></svg>Lorem ipsum lorem ipsum dolor sit ispum lorem ipsum</li>
      <li class="bullet-list__item"><svg class="bullet-list__arrow" viewBox="0 0 22 16"><path d="M1 8H19M12 1L19 8L12 15" fill="none" stroke="#29a9e0" stroke-width="2.6"/></svg>Lorem ipsum dolor sit ispum Lorem ipsum dolor sit</li>
    </ul>
  </section>

  <div class="screen-visual screen-visual--second" role="img" aria-label="Laptop displaying a website project screenshot"></div>

  <footer>
    <p class="copyright">Copyright text here</p>
    <div class="page-number"><div class="page-number__box">01</div></div>
  </footer>
</main>
</body>
</html>
```